Using attached logo that has been created

Business card with logo that's attached. Maybe with water or the cartoon van in background. Looking for it to not be so plain and not too white.
Information to include;
Rennie Ostrow
(555) 284-7163
Info@rennieswaterworks.example
www.rennieswaterworks.example
License # 4620917
Looking forward to the designs u come up with.
Thank you!
-Delphine
Target Market(s)
Plumbing
Industry/Entity Type
Plumbing
Contact Information for Business Card
Listed above

```html
<!DOCTYPE html>
<html lang="en">
<head>
<meta charset="utf-8">
<title>Rennie's Waterworks – Business Card</title>
<link rel="stylesheet" href="https://fonts.googleapis.com/css2?family=Montserrat:wght@400;500;700;800&display=swap">
<style>
  :root {
    --backdrop: #d2d6d7;
    --card-white: #efefee;
    --card-yellow: #f1b50b;
    --brand-blue: #1656b8;
    --text-grey: #6c6c6c;
    --figure-skin: #c98a63;
    --figure-shirt: #2b66c8;
    --figure-trousers: #8a7656;
  }
  * { box-sizing: border-box; margin: 0; padding: 0; }
  html, body { width: 1200px; height: 1051px; overflow: hidden; }
  body {
    background: var(--backdrop);
    font-family: "Montserrat", Arial, sans-serif;
    position: relative;
  }
  .card {
    position: absolute;
    width: 560px;
    height: 320px;
    border-bottom: 6px solid var(--brand-blue);
    box-shadow: 0 18px 40px rgba(60, 70, 75, 0.28);
  }
  .card--back {
    left: 560px; top: 240px;
    background: var(--card-yellow);
    display: flex; flex-direction: column; align-items: center; justify-content: center;
    gap: 12px;
  }
  .card--front {
    left: 90px; top: 480px;
    background: var(--card-white);
    border-bottom-width: 3px;
    display: flex; align-items: center;
  }
  .mascot {
    border-radius: 14px 14px 6px 6px;
    background: linear-gradient(180deg, var(--figure-skin) 0%, var(--figure-shirt) 38%, var(--figure-shirt) 55%, var(--figure-trousers) 100%);
  }
  .card--back .mascot { width: 120px; height: 150px; }
  .wordmark {
    font-weight: 800;
    color: var(--brand-blue);
    letter-spacing: 0.04em;
    text-transform: uppercase;
    text-align: center;
  }
  .card--back .wordmark { font-size: 24px; }
  .brand-block {
    width: 230px;
    display: flex; flex-direction: column; align-items: center; gap: 8px;
  }
  .card--front .mascot { width: 96px; height: 120px; }
  .card--front .wordmark { font-size: 17px; }
  .divider {
    width: 1.5px; height: 170px; background: var(--brand-blue);
  }
  .details { padding-left: 34px; }
  .details__name {
    font-size: 23px; font-weight: 700; color: var(--brand-blue);
    text-transform: uppercase; letter-spacing: 0.03em;
  }
  .details__license {
    font-size: 13px; color: var(--text-grey); margin-top: 4px; margin-bottom: 22px;
  }
  .contact-list { list-style: none; display: flex; flex-direction: column; gap: 7px; }
  .contact-list li {
    font-size: 13px; color: var(--text-grey);
    display: flex; align-items: center; gap: 8px;
  }
  .contact-list svg { width: 12px; height: 12px; fill: var(--brand-blue); flex: none; }
</style>
</head>
<body>
  <section class="card card--back" aria-label="Business card back">
    <div class="mascot" role="img" aria-label="Illustrated plumber mascot holding a wrench and power saw"></div>
    <p class="wordmark">Rennie's Waterworks</p>
  </section>

  <section class="card card--front" aria-label="Business card front">
    <div class="brand-block">
      <div class="mascot" role="img" aria-label="Illustrated plumber mascot holding a wrench and power saw"></div>
      <p class="wordmark">Rennie's Waterworks</p>
    </div>
    <div class="divider"></div>
    <div class="details">
      <h1 class="details__name">Rennie Ostrow</h1>
      <p class="details__license">License # 4620917</p>
      <ul class="contact-list">
        <li>
          <svg viewBox="0 0 24 24" aria-hidden="true"><path d="M6.6 10.8a15.1 15.1 0 0 0 6.6 6.6l2.2-2.2a1 1 0 0 1 1-.25 11.4 11.4 0 0 0 3.6.57 1 1 0 0 1 1 1V20a1 1 0 0 1-1 1A17 17 0 0 1 3 4a1 1 0 0 1 1-1h3.5a1 1 0 0 1 1 1c0 1.25.2 2.45.57 3.57a1 1 0 0 1-.25 1z"/></svg>
          (555) 284-7163
        </li>
        <li>
          <svg viewBox="0 0 24 24" aria-hidden="true"><path d="M2 5h20v2l-10 6L2 7z"/><path d="M2 9l10 6 10-6v10H2z"/></svg>
          Info@rennieswaterworks.example
        </li>
        <li>
          <svg viewBox="0 0 24 24" aria-hidden="true"><circle cx="12" cy="12" r="10"/></svg>
          www.rennieswaterworks.example
        </li>
      </ul>
    </div>
  </section>
</body>
</html>
```